Dryer Vent Cleaning Postcard Design

We need a postcard design for Flue Wranglers, a company that specializes in dryer vent cleaning, repairs and upgrades. Dryer vents need periodic cleaning to avoid lint clogging, dryer malfunction, long dry times and even a house fire. This card will be sent to residential and businesses prospects to introduce them to our services and the importance of maintaining their dryer vents. Our website is @ fluewrangling.com and provides information about our services, photos of our work and our general color scheme (purple/orange). Final print size will be 5x7 horizontal.

Target Market(s)

homeowners and business owners (spas, salons, grooming, gyms, laundrymats, etc)

Requirements
Must have
• Reduce the risk of fire
shortened dry times
lower energy consumption
18000 dryer fires caused in the US per year
Nice to have
• Does your dryer take too long to dry?

```html
<!DOCTYPE html>
<html lang="en">
<head>
<meta charset="utf-8">
<title>Flue Wranglers – Dryer Vent Cleaning Postcard</title>
<link rel="stylesheet" href="https://fonts.googleapis.com/css2?family=Open+Sans:wght@400;600;700;800&family=Oswald:wght@400;500&display=swap">
<style>
  :root{
    --purple:#4a3877;
    --purple-mid:#7a4f86;
    --orange:#f3894f;
    --orange-deep:#ee7a3a;
    --ink:#1d1d24;
    --white:#ffffff;
    --stage-top:#7a7a7a;
    --stage-bottom:#a3a3a3;
    --photo-dark:#3c3c3e;
    --photo-light:#8e8e90;
    --figure:#b79a72;
  }
  *{margin:0;padding:0;box-sizing:border-box}
  html,body{width:1200px;height:2761px;overflow:hidden}
  body{
    background:linear-gradient(180deg,var(--stage-top),var(--stage-bottom));
    font-family:"Open Sans",Arial,sans-serif;
    position:relative;
  }
  .card-slot{position:absolute;left:50px;width:1100px;height:769px}
  .card-slot.front{top:420px}
  .card-slot.back{top:1570px}
  .card{
    position:absolute;left:0;top:0;width:612px;height:428px;
    transform:scale(1.7974);transform-origin:0 0;
    overflow:hidden;
    box-shadow:0 3px 8px rgba(0,0,0,.35);
    background:linear-gradient(90deg,var(--purple) 0%,var(--purple-mid) 45%,var(--orange) 100%);
  }
  .card-bg{position:absolute;inset:0;width:612px;height:428px}
  .abs{position:absolute}

  /* front */
  .front-title{left:0;width:612px;top:18px;text-align:center;color:var(--white);
    font-weight:600;font-size:43px;letter-spacing:.5px;line-height:1}
  .front-sub{left:0;width:612px;top:66px;text-align:center;color:var(--white);
    font-size:15.5px;letter-spacing:.6px;font-weight:400}
  .question{left:20px;top:190px;font-family:"Oswald",sans-serif;font-size:21px;line-height:1.3;color:var(--ink);font-weight:400}
  .answer{left:22px;top:248px;color:var(--orange-deep);font-weight:700;font-size:16px}
  .answer-note{left:22px;top:270px;color:var(--ink);font-weight:600;font-size:11.5px}
  .photo-label{color:var(--white);font-weight:700;font-size:10px;text-align:center;line-height:1.25;text-shadow:0 1px 2px rgba(0,0,0,.6)}
  .brand{display:flex;align-items:center;gap:6px;color:var(--purple);font-weight:800;font-size:17px}
  .brand-dot{width:14px;height:14px;border-radius:50%;background:var(--orange)}
  .cta-bar{left:250px;top:350px;width:326px;height:38px;border-radius:0 19px 19px 0;
    background:linear-gradient(90deg,var(--orange),var(--purple));
    color:var(--white);font-weight:700;font-size:14px;display:flex;align-items:center;padding-left:32px}
  .cta-phone-dot{left:230px;top:346px;width:46px;height:46px;border-radius:50%;background:var(--orange);
    border:3px solid var(--white);display:flex;align-items:center;justify-content:center}
  .contact{display:flex;align-items:center;gap:5px;color:var(--ink);font-weight:700}
  .front .contact{font-size:9.5px}
  .back .contact{font-size:12.5px}

  /* back */
  .back-title{left:0;width:612px;top:30px;text-align:center;color:var(--white);font-weight:700;font-size:22px}
  .benefits{left:150px;top:76px;list-style:none;color:var(--white);font-size:13.5px}
  .benefits li{display:flex;align-items:flex-start;gap:10px;height:30px;line-height:1.1}
  .benefit-icon{flex:none;width:22px;height:22px;border-radius:50%;border:2px solid var(--white);
    display:flex;align-items:center;justify-content:center}
  .figure{left:0;top:145px;width:120px;height:290px;border-radius:40px 40px 6px 6px;
    background:linear-gradient(180deg,#c9ad86,var(--figure) 60%,#7a5a3a)}
  .cta-box{left:112px;top:228px;width:260px;height:62px;border-radius:0 12px 12px 0;background:var(--orange-deep);
    text-align:center;padding-top:6px}
  .cta-box .cta-label{color:var(--white);font-weight:700;font-size:15px;line-height:1.1}
  .cta-box .cta-number{color:var(--ink);font-weight:700;font-size:26px;line-height:1.2}
</style>
</head>
<body>

<!-- FRONT -->
<section class="card-slot front">
  <div class="card front">
    <svg class="card-bg" viewBox="0 0 612 428" aria-hidden="true">
      <path d="M0 90 C140 78 260 110 340 170 C420 232 520 296 612 316 L612 428 L0 428 Z" fill="#ffffff"/>
      <path d="M0 82 C140 70 262 102 344 162" fill="none" stroke="#f3894f" stroke-width="4"/>
    </svg>

    <h1 class="abs front-title">DRYER VENT CLEANING</h1>
    <p class="abs front-sub">YOUR PROFESSIONAL DRYER VENT CLEANING SOLUTION</p>

    <svg class="abs" style="left:0;top:0" width="612" height="428" viewBox="0 0 612 428">
      <defs>
        <radialGradient id="ductShade" cx="50%" cy="45%" r="55%">
          <stop offset="0" stop-color="#1e1e20"/>
          <stop offset=".5" stop-color="#3c3c3e"/>
          <stop offset="1" stop-color="#9a9a9c"/>
        </radialGradient>
      </defs>
      <circle cx="306" cy="205" r="67" fill="url(#ductShade)" stroke="#fff" stroke-width="4" role="img" aria-label="Photo looking into a clogged dryer vent duct"/>
      <circle cx="468" cy="217" r="98" fill="url(#ductShade)" stroke="#fff" stroke-width="4" role="img" aria-label="Photo looking into a clean dryer vent duct"/>
    </svg>
    <p class="abs photo-label" style="left:256px;top:236px;width:100px">CLOGGED<br>DRYER VENTS</p>
    <p class="abs photo-label" style="left:418px;top:274px;width:100px">CLEAN<br>DRYER VENT</p>

    <p class="abs question">DOES YOUR DRYER<br>TAKE TOO LONG TO DRY?</p>
    <p class="abs answer">IF YOU SAID “YES,”</p>
    <p class="abs answer-note">you may have a dirty dryer vent!</p>

    <div class="abs brand" style="left:40px;top:352px"><span class="brand-dot"></span>Flue Wranglers</div>

    <div class="abs cta-bar">CALL FOR A QUOTE - 555-014-2290</div>
    <div class="abs cta-phone-dot">
      <svg width="20" height="20" viewBox="0 0 24 24" aria-hidden="true"><path fill="#4a3877" d="M6.6 10.8a15.1 15.1 0 0 0 6.6 6.6l2.2-2.2a1 1 0 0 1 1-.25 11.4 11.4 0 0 0 3.6.57 1 1 0 0 1 1 1V20a1 1 0 0 1-1 1A17 17 0 0 1 3 4a1 1 0 0 1 1-1h3.5a1 1 0 0 1 1 1c0 1.25.2 2.45.57 3.57a1 1 0 0 1-.25 1z"/></svg>
    </div>

    <div class="abs contact" style="left:244px;top:400px">
      <svg width="12" height="9" viewBox="0 0 12 9" aria-hidden="true"><rect width="12" height="9" fill="#4a3877"/><path d="M0 0 L6 5 L12 0" fill="none" stroke="#fff" stroke-width="1"/></svg>
      office@fluewrangling.com
    </div>
    <div class="abs contact" style="left:398px;top:400px">
      <svg width="11" height="11" viewBox="0 0 12 12" aria-hidden="true"><g fill="none" stroke="#4a3877" stroke-width="1.2"><circle cx="6" cy="6" r="5.2"/><ellipse cx="6" cy="6" rx="2.3" ry="5.2"/><path d="M1 6h10"/></g></svg>
      www.office@fluewrangling.com
    </div>
  </div>
</section>

<!-- BACK -->
<section class="card-slot back">
  <div class="card back">
    <svg class="card-bg" viewBox="0 0 612 428" aria-hidden="true">
      <path d="M0 360 C200 300 420 232 612 150 L612 428 L0 428 Z" fill="#ffffff"/>
      <path d="M0 352 C200 292 420 224 612 142" fill="none" stroke="#f3894f" stroke-width="4"/>
    </svg>

    <h2 class="abs back-title">WHY IS DRYER VENT CLEANING IMPORTANT?</h2>

    <ul class="abs benefits">
      <li><span class="benefit-icon"><svg width="10" height="12" viewBox="0 0 10 12" aria-hidden="true"><path d="M5 0 C7 3 9 5 9 8 A4 4 0 0 1 1 8 C1 6 2 5 3 4 C3 6 4 6 5 6 C5 4 4 2 5 0Z" fill="#fff"/></svg></span>Reduce the risk of fire</li>
      <li><span class="benefit-icon"><svg width="12" height="12" viewBox="0 0 12 12" aria-hidden="true"><circle cx="6" cy="6" r="4.5" fill="none" stroke="#fff" stroke-width="1.4"/><path d="M6 3v3l2 1.5" stroke="#fff" stroke-width="1.4" fill="none"/></svg></span>Shortened dry times</li>
      <li><span class="benefit-icon"><svg width="12" height="12" viewBox="0 0 12 12" aria-hidden="true"><path d="M7 0 L2 7 H6 L5 12 L10 5 H6 Z" fill="#fff"/></svg></span>Lower energy consumption</li>
      <li style="height:36px"><span class="benefit-icon"><svg width="12" height="12" viewBox="0 0 12 12" aria-hidden="true"><rect x="1" y="1" width="10" height="10" rx="1.5" fill="none" stroke="#fff" stroke-width="1.3"/><circle cx="6" cy="7" r="2.5" fill="none" stroke="#fff" stroke-width="1.2"/></svg></span>18000 dryer fires caused in the US<br>per year</li>
    </ul>

    <svg class="abs" style="left:0;top:0" width="612" height="428" viewBox="0 0 612 428">
      <defs>
        <linearGradient id="atticShade" x1="0" y1="0" x2="1" y2="1">
          <stop offset="0" stop-color="#6f6a63"/>
          <stop offset=".5" stop-color="#a9a7a4"/>
          <stop offset="1" stop-color="#3e3a35"/>
        </linearGradient>
      </defs>
      <circle cx="514" cy="230" r="82" fill="url(#atticShade)" stroke="#f3894f" stroke-width="4" role="img" aria-label="Photo of foil dryer vent ducting in an attic"/>
      <circle cx="425" cy="318" r="53" fill="url(#atticShade)" stroke="#f3894f" stroke-width="4" role="img" aria-label="Photo of flexible dryer vent hose under a house"/>
    </svg>

    <div class="abs figure" role="img" aria-label="Cartoon vent technician holding a cleaning brush"></div>

    <div class="abs cta-box">
      <p class="cta-label">CALL FOR A QUOTE</p>
      <p class="cta-number">555-014-2290</p>
    </div>

    <div class="abs brand" style="left:152px;top:350px"><span class="brand-dot"></span>Flue Wranglers</div>

    <div class="abs contact" style="left:150px;top:406px">
      <svg width="14" height="10" viewBox="0 0 12 9" aria-hidden="true"><rect width="12" height="9" fill="#4a3877"/><path d="M0 0 L6 5 L12 0" fill="none" stroke="#fff" stroke-width="1"/></svg>
      office@fluewrangling.com
    </div>
    <div class="abs contact" style="left:355px;top:406px">
      <svg width="13" height="13" viewBox="0 0 12 12" aria-hidden="true"><g fill="none" stroke="#4a3877" stroke-width="1.2"><circle cx="6" cy="6" r="5.2"/><ellipse cx="6" cy="6" rx="2.3" ry="5.2"/><path d="M1 6h10"/></g></svg>
      www.office@fluewrangling.com
    </div>
  </div>
</section>

</body>
</html>
```